Every Drawer Neatly Sorted or EDN Organized needs a business card design. EDN Organized is a professi

We need a business card design that is clean, sharp and conveys a sense of organization. I already have a logo.

Target Market(s)

Families (specifically mothers), small business owners, parents, seniors

Industry/Entity Type

Business

Contact Information for Business Card

My website is www.ednorganized-example.com and my Facebook page is http://www.socialpage-example.com/everydrawerneatlysorted. The phone number is 555-418-2706 and I want to be listed as Miriel O. Dunsford, Owner

Requirements
Must have
• My logo.

```html
<!DOCTYPE html>
<html lang="en">
<head>
<meta charset="UTF-8">
<title>EDN Organized – Business Card</title>
<link href="https://fonts.googleapis.com/css2?family=Montserrat:wght@400&family=Open+Sans:ital,wght@0,400;0,600;1,700&display=swap" rel="stylesheet">
<style>
  :root {
    --page-bg: #e8e6e4;
    --card-bg: #1f2a35;
    --ink: #f3f3f3;
    --ink-soft: #e2e4e6;
    --accent: #1b7fd8;
  }
  html, body {
    margin: 0;
    width: 1200px;
    height: 900px;
    overflow: hidden;
    background: var(--page-bg);
  }
  .business-card {
    position: absolute;
    left: 105px;
    top: 142px;
    width: 990px;
    height: 615px;
    background: var(--card-bg);
    box-shadow: 0 6px 24px rgba(0,0,0,0.18);
    font-family: "Open Sans", Arial, sans-serif;
    color: var(--ink);
  }
  .brand {
    position: absolute;
    left: 40px;
    top: 190px;
    width: 470px;
    text-align: center;
    font-family: "Montserrat", Arial, sans-serif;
    font-weight: 400;
    color: var(--ink);
  }
  .brand-initials {
    font-size: 64px;
    line-height: 1;
    letter-spacing: 4px;
    margin: 0 0 22px;
  }
  .brand-name {
    font-size: 26px;
    line-height: 1.2;
    letter-spacing: 2px;
    margin: 0;
  }
  .person {
    position: absolute;
    left: 560px;
    top: 128px;
  }
  .person-name {
    font-size: 32px;
    font-weight: 600;
    line-height: 1.2;
    margin: 0;
  }
  .person-title {
    font-size: 26px;
    line-height: 1.2;
    margin: 0;
    color: var(--ink-soft);
  }
  .contact-list {
    position: absolute;
    left: 566px;
    top: 258px;
    margin: 0;
    padding: 0;
    list-style: none;
    font-size: 24px;
    line-height: 37px;
  }
  .contact-item {
    display: flex;
    align-items: center;
    white-space: nowrap;
  }
  .contact-item.social { margin-top: 40px; }
  .contact-icon {
    width: 16px;
    height: 16px;
    margin-right: 12px;
    flex: none;
    fill: var(--ink);
  }
  .tagline {
    position: absolute;
    left: 0;
    right: 0;
    top: 498px;
    margin: 0;
    text-align: center;
    padding-left: 20px;
    font-size: 26px;
    font-style: italic;
    font-weight: 700;
    color: var(--accent);
  }
</style>
</head>
<body>
  <section class="business-card">
    <div class="brand">
      <p class="brand-initials">EDN</p>
      <p class="brand-name">Every Drawer Neatly Sorted</p>
    </div>

    <div class="person">
      <p class="person-name">Miriel O. Dunsford</p>
      <p class="person-title">Owner</p>
    </div>

    <ul class="contact-list">
      <li class="contact-item">
        <svg class="contact-icon" viewBox="0 0 16 16" aria-hidden="true"><path d="M3.2 1.2l2.4 2.6-1.3 1.9c.9 2 2.6 3.7 4.6 4.6l1.9-1.3 2.6 2.4-1.4 2.6C6.6 13.6 2.4 9.4 1 3.2z"/></svg>
        555-418-2706
      </li>
      <li class="contact-item">
        <svg class="contact-icon" viewBox="0 0 16 16" aria-hidden="true"><path d="M1 3h14v10H1z M2 4l6 4.5L14 4v-.01H2z" fill-rule="evenodd"/></svg>
        hello@tidyhome-example.com
      </li>
      <li class="contact-item">
        <svg class="contact-icon" viewBox="0 0 16 16" aria-hidden="true"><circle cx="8" cy="8" r="7"/></svg>
        www.ednorganized-example.com
      </li>
      <li class="contact-item social">
        <svg class="contact-icon" viewBox="0 0 16 16" aria-hidden="true"><circle cx="8" cy="8" r="6"/></svg>
        everydrawerneatlysorted
      </li>
    </ul>

    <p class="tagline">Calm spaces for busy lives, one drawer at a time</p>
  </section>
</body>
</html>
```